Business Card design for an International Import Export House

We need a Business Card design for our import export business. We trade in Minerals, Metals, Rice, Sugar, Steel etc.. The design should be minimalistic. It may or may not contain the physical address. In case you want to include the physical address - 418 Verandah Heights, Marlow Sector 9, Aravali District, India, 404117.

Target Market(s)

Steel Mills or Steel Plants, Factories, Mining businesses, Industrial houses, Government Agencies

Industry/Entity Type

Importer

Contact Information for Business Card

Business Name - Veltrane Overseas

Font styles to use
Other font styles liked:
• montserrat

Requirements
Must have
• Ravi Kandola - President
• www.veltraneoverseas.com
• ravi@veltraneoverseas.com
• +91-987-654-3217
Nice to have
• worldwide suppliers of ores

```html
<!DOCTYPE html>
<html lang="en">
<head>
<meta charset="utf-8">
<title>Veltrane Overseas — Stationery</title>
<link rel="stylesheet" href="https://fonts.googleapis.com/css2?family=Montserrat:wght@400;500;600;700&family=Open+Sans:wght@400;600&display=swap">
<style>
  :root {
    --backdrop: #eceeef;
    --paper: #ffffff;
    --teal: #2f8799;
    --teal-faint: #dbe8ec;
    --ink: #3a3d40;
    --ink-soft: #6b7075;
    --rule: #cfd6d9;
  }
  * { box-sizing: border-box; margin: 0; padding: 0; }
  html, body {
    width: 1200px; height: 793px; overflow: hidden;
    background: var(--backdrop);
    font-family: "Open Sans", Arial, sans-serif;
    color: var(--ink);
  }
  .canvas { position: relative; width: 1200px; height: 793px; }

  /* Brand lockup */
  .brand { display: flex; align-items: center; gap: 7px; }
  .brand-dot { border-radius: 50%; background: var(--teal); flex: none; }
  .brand-name {
    font-family: "Montserrat", Arial, sans-serif;
    font-weight: 600; letter-spacing: 0.04em; text-transform: uppercase;
    color: var(--teal); white-space: nowrap;
  }

  /* Letterhead */
  .letterhead {
    position: absolute; left: 80px; top: 36px;
    width: 509px; height: 720px;
    background: var(--paper);
    box-shadow: 0 1px 3px rgba(0,0,0,0.12);
    overflow: hidden;
  }
  .letterhead .brand { position: absolute; left: 48px; top: 52px; }
  .letterhead .brand-dot { width: 16px; height: 16px; }
  .letterhead .brand-name { font-size: 10px; }
  .letterhead-mark {
    position: absolute; right: -40px; top: 190px;
    width: 230px; height: 230px; border-radius: 50%;
    background: var(--teal-faint); opacity: 0.55;
  }
  .letter {
    position: absolute; left: 48px; top: 110px; width: 360px;
    font-size: 7.4px; line-height: 1.55; color: var(--ink);
  }
  .letter-date { margin-bottom: 14px; }
  .letter-recipient { margin-bottom: 18px; font-style: normal; }
  .letter-salutation { margin-bottom: 8px; }
  .letter-body p { margin-bottom: 8px; text-align: justify; }
  .letter-closing { margin-top: 10px; }
  .signature {
    width: 90px; height: 26px; margin-top: 10px;
    background: linear-gradient(90deg, #e9ecee, #f4f5f6);
    border-radius: 3px;
  }
  .signer-title { font-size: 8px; margin-top: 3px; }
  .letterhead-footer {
    position: absolute; right: 40px; bottom: 40px;
    text-align: right; font-size: 6.4px; line-height: 1.7;
    font-family: "Montserrat", Arial, sans-serif; color: var(--ink);
    white-space: nowrap;
  }

  /* Business cards */
  .card {
    position: absolute; width: 350px; height: 200px;
    box-shadow: 0 1px 3px rgba(0,0,0,0.14);
  }
  .card-front {
    left: 700px; top: 120px; background: var(--teal);
    display: flex; align-items: center; justify-content: center;
  }
  .card-front .brand { flex-direction: column; gap: 12px; }
  .card-front .brand-dot { width: 34px; height: 34px; background: var(--paper); }
  .card-front .brand-name { color: var(--paper); font-size: 15px; }

  .card-back { left: 700px; top: 440px; background: var(--paper); }
  .card-back .brand {
    position: absolute; left: 26px; top: 86px;
    flex-direction: column; align-items: flex-start; gap: 8px;
  }
  .card-back .brand-dot { width: 22px; height: 22px; }
  .card-back .brand-name { font-size: 9.5px; }
  .card-divider {
    position: absolute; left: 168px; top: 30px; width: 1px; height: 140px;
    background: var(--rule);
  }
  .card-person { position: absolute; left: 186px; top: 38px; }
  .person-name {
    font-family: "Montserrat", Arial, sans-serif;
    font-weight: 600; font-size: 12px; color: var(--teal);
  }
  .person-role {
    font-family: "Montserrat", Arial, sans-serif;
    font-size: 8px; color: var(--ink-soft); margin-top: 2px;
  }
  .card-contact {
    position: absolute; left: 186px; top: 92px; width: 155px;
    list-style: none; font-family: "Montserrat", Arial, sans-serif;
    font-size: 7px; line-height: 1.75; color: var(--ink);
    white-space: nowrap;
  }
</style>
</head>
<body>
<main class="canvas">

  <section class="letterhead">
    <div class="letterhead-mark" aria-hidden="true"></div>
    <div class="brand">
      <span class="brand-dot"></span>
      <span class="brand-name">Veltrane Overseas</span>
    </div>

    <article class="letter">
      <p class="letter-date">November 14, 2024</p>
      <address class="letter-recipient">
        The Purchasing Manager<br>
        Eastfield Steel Works<br>
        Plot 12, Industrial Area
      </address>
      <p class="letter-salutation">Dear Sir,</p>
      <div class="letter-body">
        <p>Thank you for your recent enquiry regarding iron ore and steel billet supplies. Veltrane Overseas works with trusted mines and mills across Asia, Africa and South America to deliver consistent grades on schedule. We handle inspection, documentation and freight so your plant receives material ready for use.</p>
        <p>Please find our current price schedule attached for the coming quarter. Rates cover shipments of ten thousand tonnes and above, with flexible terms for long contracts. Our team would welcome the chance to visit your works and discuss volumes, delivery ports and quality requirements in detail.</p>
        <p>We look forward to building a lasting partnership with your company.</p>
      </div>
      <p class="letter-closing">Sincerely,</p>
      <div class="signature" role="img" aria-label="Handwritten signature"></div>
      <p class="signer-title">President</p>
    </article>

    <footer class="letterhead-footer">
      418 Verandah Heights, Marlow Sector 9, Aravali District, India, 404117<br>
      +91-987-654-3217 &nbsp;|&nbsp; ravi@veltraneoverseas.com &nbsp;|&nbsp; www.veltraneoverseas.com
    </footer>
  </section>

  <section class="card card-front">
    <div class="brand">
      <span class="brand-dot"></span>
      <span class="brand-name">Veltrane Overseas</span>
    </div>
  </section>

  <section class="card card-back">
    <div class="brand">
      <span class="brand-dot"></span>
      <span class="brand-name">Veltrane Overseas</span>
    </div>
    <div class="card-divider"></div>
    <div class="card-person">
      <p class="person-name">Ravi Kandola</p>
      <p class="person-role">President</p>
    </div>
    <ul class="card-contact">
      <li>418 Verandah Heights, Marlow Sector 9,</li>
      <li>Aravali District, India, 404117</li>
      <li>+91-987-654-3217</li>
      <li>ravi@veltraneoverseas.com</li>
      <li>www.veltraneoverseas.com</li>
    </ul>
  </section>

</main>
</body>
</html>
```